Student Business Card Design

As you already know, I'm a student at BV majoring in Supply Chain & Logistics Technology. I want a business card design that leaves the recipient impressed. A clean, professional, and memorable design is desired without too much color. My school's logo can be found online. I'd like to have that on the card.

Target Market(s)

Anyone who is a recruiter or an employer who has authority to hire.

Industry/Entity Type

Business

Contact Information for Business Card

Name: Osman Velibor

Phone Number: 614-275-3316

Email Address: velibor.osman@mailbox-demo.net

Major: Supply Chain & Logistics Technology

Minor: Purchasing

University: Marlowe State University

College: Ashcombe School of Engineering

I want a Workvine logo with my name beside it.

Also, on the back of the card I want this quote: "If it doesn't challenge you, it doesn't change you"-, Lena Sorbach

Requirements
Must have
• I'd like to see a Workvine logo go with my name.
• Professional-I'm going to be handing this card out in career fairs and networking events.
Nice to have
• Marlowe State University's colors: white, silver, and red, but if you feel it's better to go with a different color scheme then do it.
Should not have
• No white space on the design.

```html
<!DOCTYPE html>
<html lang="en">
<head>
<meta charset="utf-8">
<title>Osman Velibor – Business Card</title>
<link rel="stylesheet" href="https://fonts.googleapis.com/css2?family=Arimo:wght@400;700&family=Tinos:ital@1&display=swap">
<style>
  :root {
    --card: #4a4a4a;
    --divider: #8a8a8a;
    --white: #ffffff;
    --soft: #dcdcdc;
    --muted: #a9a9a9;
    --quote-mark: #6a6a6a;
  }
  * { margin: 0; padding: 0; box-sizing: border-box; }
  html, body {
    width: 1200px; height: 350px; overflow: hidden;
    background: var(--card);
  }
  .sheet {
    position: relative; width: 1200px; height: 350px;
    display: flex;
    font-family: "Arimo", Arial, sans-serif;
  }
  .card { position: relative; height: 350px; background: var(--card); }
  .card--front { width: 598px; }
  .card--back { width: 592px; }
  .divider { width: 10px; height: 350px; background: var(--divider); }

  .brand {
    position: absolute; left: 32px; top: 80px;
    display: flex; align-items: center; gap: 6px;
    color: var(--white); font-size: 15px; font-weight: 400;
  }
  .brand__square { width: 14px; height: 14px; background: var(--white); border-radius: 2px; }

  .name {
    position: absolute; left: 120px; top: 74px;
    color: var(--white); font-size: 32px; font-weight: 400; letter-spacing: -0.5px;
    white-space: nowrap;
  }
  .name__last { font-weight: 700; }

  .role {
    position: absolute; left: 172px; top: 128px;
    color: var(--white); font-size: 18px;
  }
  .role__label { font-weight: 700; margin-right: 8px; }

  .contact {
    position: absolute; left: 252px; top: 154px;
    color: var(--soft); font-size: 17px; line-height: 29px; list-style: none;
  }

  .school {
    position: absolute; left: 252px; top: 226px;
    color: var(--soft);
  }
  .school__name { font-size: 19px; letter-spacing: 0.5px; font-weight: 400; }
  .school__college { font-size: 11px; letter-spacing: 0.5px; margin-top: 4px; color: var(--muted); }

  .quote-mark {
    position: absolute; left: 58px; top: 40px;
    font-family: "Tinos", "Times New Roman", serif; font-style: italic;
    font-size: 190px; line-height: 1; color: var(--quote-mark);
  }
  .quote {
    position: absolute; right: 100px; top: 128px;
    text-align: right;
    font-family: "Tinos", "Times New Roman", serif; font-style: italic;
    color: var(--white); font-size: 29px; line-height: 34px;
  }
  .quote__author {
    display: block; margin-top: 10px;
    font-style: normal; font-size: 22px; color: var(--muted);
    padding-right: 18px;
  }
</style>
</head>
<body>
<main class="sheet">
  <section class="card card--front">
    <div class="brand"><span class="brand__square"></span>Workvine</div>
    <h1 class="name">Osman <span class="name__last">Velibor</span></h1>
    <p class="role"><span class="role__label">Student</span>Supply Chain Logistics, Purchasing</p>
    <ul class="contact">
      <li>velibor.osman@mailbox-demo.net</li>
      <li>614-275-3316</li>
    </ul>
    <div class="school">
      <div class="school__name">MARLOWE STATE UNIVERSITY</div>
      <div class="school__college">ASHCOMBE SCHOOL OF ENGINEERING</div>
    </div>
  </section>
  <div class="divider"></div>
  <section class="card card--back">
    <span class="quote-mark" aria-hidden="true">“</span>
    <blockquote class="quote">
      If it doesn’t challenge you,<br>
      it doesn’t change you.
      <cite class="quote__author">Lena Sorbach</cite>
    </blockquote>
  </section>
</main>
</body>
</html>
```